business cards and stationary
Quorvane Motion Collective
Professional
Matthew L. Dorsand, D.C.
Chiropractor
4817 Halvering Crest Avenue
Los Angeles, CA 90048
mldorsand@quorvanemotion.example
Quorvanemotion.example
CA74829
map of location
logo file .AI

```html
<!DOCTYPE html>
<html lang="en">
<head>
<meta charset="utf-8">
<title>Quorvane Motion Collective – Stationery</title>
<link href="https://fonts.googleapis.com/css2?family=Montserrat:wght@700&family=Open+Sans:wght@400;600&display=swap" rel="stylesheet">
<style>
:root{
  --orange:#f7941d;
  --grey:#6d6e71;
  --grey-light:#a7a9ac;
  --paper:#ffffff;
  --bg-dark:#2f3031;
  --bg-mid:#7d7e80;
  --bg-light:#a4a5a7;
  --label:#d9d9d9;
  --map-a:#e8e4d8;
  --map-b:#d6dccb;
}
*{margin:0;padding:0;box-sizing:border-box}
html,body{width:1200px;height:382px;overflow:hidden}
body{font-family:"Open Sans",Arial,sans-serif;color:var(--grey)}
.board{position:relative;width:1200px;height:382px;
  background:radial-gradient(ellipse at 70% 45%,var(--bg-light) 0%,var(--bg-mid) 45%,var(--bg-dark) 100%)}
.piece{position:absolute;background:var(--paper);box-shadow:0 3px 8px rgba(0,0,0,.45);overflow:hidden}
.label{position:absolute;font-size:5px;color:var(--label);text-align:center;white-space:nowrap}
.wordmark{font-family:"Montserrat",Arial,sans-serif;font-weight:700;color:var(--orange);line-height:1;display:flex;align-items:center;gap:3px;white-space:nowrap}
.wordmark .dot{display:inline-block;border-radius:50%;background:var(--orange);flex:none}
.name{font-weight:600}
.wave{position:absolute;left:0;bottom:0;width:100%}

/* brand block */
.brand{position:absolute;left:26px;top:72px}
.brand .wordmark{font-size:46px;gap:8px}
.brand .wordmark .dot{width:14px;height:14px}
.brand .tagline{font-family:"Montserrat",Arial,sans-serif;font-weight:700;color:var(--orange);font-size:12px;margin-top:4px;padding-left:22px;letter-spacing:.4px}
.caption{position:absolute;left:150px;top:156px;font-size:5px;color:var(--label)}

/* cards */
.card{width:140px;height:78px}
.card .map{position:absolute;inset:0;background:linear-gradient(135deg,var(--map-a),var(--map-b))}
.card-orange{background:var(--orange);display:flex;align-items:center;justify-content:center}
.card-orange .wordmark{font-size:18px;color:var(--paper)}
.card-orange .wordmark .dot{width:6px;height:6px;background:var(--paper)}
.card .wordmark.small{position:absolute;left:7px;top:9px;font-size:9px}
.card .wordmark.small .dot{width:4px;height:4px}
.card .details{position:absolute;left:74px;top:8px;font-size:3.6px;line-height:1.55;white-space:nowrap}
.card .wave{height:18px}

/* letterheads */
.letter{width:258px;height:334px;top:18px}
.letter .wordmark{position:absolute;left:14px;top:14px;font-size:14px}
.letter .wordmark .dot{width:5px;height:5px}
.letter .sender{position:absolute;left:140px;top:12px;font-size:3.6px;line-height:1.55;white-space:nowrap}
.letter .wave{height:40px}
.letter .footer-text{position:absolute;left:0;right:0;bottom:5px;text-align:center;font-size:3.4px;color:var(--paper);white-space:nowrap}

/* envelopes */
.env{width:300px;left:876px}
.env .flap{position:absolute;left:0;top:0;width:100%}
.env .wordmark{position:absolute;font-size:12px}
.env .wordmark .dot{width:4px;height:4px}
.env .to{position:absolute;font-size:3.6px;line-height:1.55;white-space:nowrap}
.env .wave{height:20px}
</style>
</head>
<body>
<main class="board">

  <section class="brand">
    <div class="wordmark"><span class="dot"></span>Quorvane</div>
    <div class="tagline">Motion Collective</div>
  </section>
  <div class="caption">Business Template</div>

  <!-- business cards -->
  <div class="piece card" style="left:18px;top:170px">
    <div class="map" role="img" aria-label="Map showing the office location"></div>
  </div>
  <div class="label" style="left:18px;top:251px;width:140px">Card back</div>

  <div class="piece card" style="left:170px;top:170px">
    <div class="wordmark small"><span class="dot"></span>Quorvane</div>
    <div class="details">
      <div class="name">Matthew L. Dorsand, D.C.</div>
      <div>Chiropractor</div>
      <div>4817 Halvering Crest Avenue</div>
      <div>Los Angeles, CA 90048</div>
      <div>Tel 310.555.0148</div>
      <div>mldorsand@quorvanemotion.example</div>
    </div>
    <svg class="wave" viewBox="0 0 140 18" preserveAspectRatio="none">
      <path d="M0 9 Q70 -1 140 11 L140 18 L0 18Z" fill="var(--orange)"/>
      <path d="M0 6 Q70 -4 140 8" fill="none" stroke="var(--grey-light)" stroke-width="1"/>
    </svg>
  </div>
  <div class="label" style="left:170px;top:251px;width:140px">Card front</div>

  <div class="piece card card-orange" style="left:18px;top:266px">
    <div class="wordmark"><span class="dot"></span>Quorvane</div>
  </div>
  <div class="label" style="left:18px;top:347px;width:140px">Card back</div>

  <div class="piece card" style="left:170px;top:266px">
    <div class="wordmark small"><span class="dot"></span>Quorvane</div>
    <div class="details">
      <div class="name">Matthew L. Dorsand, D.C.</div>
      <div>Chiropractor</div>
      <div>4817 Halvering Crest Avenue</div>
      <div>Los Angeles, CA 90048</div>
      <div>Quorvanemotion.example</div>
      <div>Lic. CA74829</div>
    </div>
    <svg class="wave" viewBox="0 0 140 18" preserveAspectRatio="none">
      <path d="M0 9 Q70 -1 140 11 L140 18 L0 18Z" fill="var(--orange)"/>
      <path d="M0 6 Q70 -4 140 8" fill="none" stroke="var(--grey-light)" stroke-width="1"/>
    </svg>
  </div>
  <div class="label" style="left:170px;top:347px;width:140px">Card front</div>

  <!-- letterheads -->
  <div class="piece letter" style="left:330px">
    <div class="wordmark"><span class="dot"></span>Quorvane</div>
    <div class="sender">
      <div class="name">Matthew L. Dorsand, D.C.</div>
      <div>4817 Halvering Crest Avenue</div>
      <div>Los Angeles, CA 90048</div>
      <div>Tel 310.555.0148</div>
      <div>Fax 310.555.0149</div>
    </div>
    <svg class="wave" viewBox="0 0 258 40" preserveAspectRatio="none">
      <path d="M0 16 Q129 2 258 20 L258 40 L0 40Z" fill="var(--orange)"/>
      <path d="M0 12 Q129 -2 258 16" fill="none" stroke="var(--grey-light)" stroke-width="1.2"/>
    </svg>
    <div class="footer-text">mldorsand@quorvanemotion.example · Quorvanemotion.example</div>
  </div>
  <div class="label" style="left:330px;top:356px;width:258px">Letterhead page 1</div>

  <div class="piece letter" style="left:600px">
    <div class="wordmark"><span class="dot"></span>Quorvane</div>
    <svg class="wave" viewBox="0 0 258 40" preserveAspectRatio="none">
      <path d="M0 16 Q129 2 258 20 L258 40 L0 40Z" fill="var(--orange)"/>
      <path d="M0 12 Q129 -2 258 16" fill="none" stroke="var(--grey-light)" stroke-width="1.2"/>
    </svg>
    <div class="footer-text">Quorvanemotion.example</div>
  </div>
  <div class="label" style="left:600px;top:356px;width:258px">Letterhead page 2</div>

  <!-- envelopes -->
  <div class="piece env" style="top:14px;height:72px">
    <svg class="flap" viewBox="0 0 300 30" height="30" preserveAspectRatio="none">
      <path d="M0 0 H300 V10 L150 30 L0 10Z" fill="var(--grey)"/>
    </svg>
    <div class="to" style="left:120px;top:42px">
      <div>Recipient Name</div><div>Street Address</div><div>City, State Zip</div>
    </div>
  </div>
  <div class="label" style="left:876px;top:88px;width:300px">Envelope back</div>

  <div class="piece env" style="top:98px;height:70px">
    <svg class="flap" viewBox="0 0 300 26" height="26" preserveAspectRatio="none">
      <path d="M0 0 H300 V6 L150 26 L0 6Z" fill="var(--orange)"/>
    </svg>
    <div class="to" style="left:120px;top:42px">
      <div>Recipient Name · Street Address</div>
    </div>
  </div>
  <div class="label" style="left:876px;top:170px;width:300px">Envelope open</div>

  <div class="piece env" style="top:182px;height:66px">
    <svg class="flap" viewBox="0 0 300 66" height="66" preserveAspectRatio="none">
      <path d="M0 0 L150 30 L300 0" fill="none" stroke="#d4d4d4" stroke-width="1"/>
      <path d="M0 66 L128 34 M300 66 L172 34" fill="none" stroke="#e3e3e3" stroke-width="1"/>
    </svg>
  </div>
  <div class="label" style="left:876px;top:250px;width:300px">Envelope flap</div>

  <div class="piece env" style="top:262px;height:86px">
    <div class="wordmark" style="left:10px;top:10px"><span class="dot"></span>Quorvane</div>
    <div class="to" style="left:10px;top:27px">
      <div>4817 Halvering Crest Avenue</div><div>Los Angeles, CA 90048</div>
    </div>
    <svg class="wave" viewBox="0 0 300 20" preserveAspectRatio="none">
      <path d="M0 10 Q150 -2 300 12 L300 20 L0 20Z" fill="var(--orange)"/>
      <path d="M0 7 Q150 -5 300 9" fill="none" stroke="var(--grey-light)" stroke-width="1"/>
    </svg>
  </div>
  <div class="label" style="left:876px;top:351px;width:300px">Envelope front</div>

</main>
</body>
</html>
```